Lorna Tess Tresses Fancy Business Card’s

I want my business cards to be elite, original and very classy. I want the business cards to match the colors of my logo and to match the design posted. I would love the design of the picture I posted

I want the card all white .
The dripping on the top of the card I want it to match the pink color in my logo that’s also posted .
I need my logo on the business card !
I need my Instagram- @lorna.tess.tresses__
And my phone number - 582 907 3365

Target Market(s)

My target market is young woman age 23 to older woman to the age of 65
I want both older and younger women to love my design . I don’t want any cheap looking business cards

Industry/Entity Type

Hair And Beauty

Contact Information for Business Card

Add my logo
Add my Instagram- @lorna.tess.tresses__
My number - 582 907 3365
My website- www.lornatesstresses.example

Font styles to use
Serif
Script

Colors
ffffff
e667a6
e34298

Requirements
Must have
• The business cards must have my logo, my number , my website, and my Instagram!
Nice to have
• Nice to have glitter words that match my logo
• The business cards must look classy and mature
• I want them to be very unique!!
Should not have
• Should not have any colors that doesn’t match my logo ! This is very important! Please

```html
<!DOCTYPE html>
<html lang="en">
<head>
<meta charset="utf-8">
<title>Lorna Tess Tresses – Business Card</title>
<link rel="stylesheet" href="https://fonts.googleapis.com/css2?family=Playfair+Display:wght@500&family=Montserrat:wght@400;500&display=swap">
<style>
  :root {
    --backdrop: #2b2a2b;
    --card: #ffffff;
    --pink: #e34298;
    --pink-soft: #e667a6;
    --ink-grey: #6f6f72;
    --line-grey: #9a9a9e;
  }
  * { box-sizing: border-box; margin: 0; padding: 0; }
  html, body {
    width: 1200px;
    height: 930px;
    overflow: hidden;
    background: var(--backdrop);
  }
  .stage {
    position: relative;
    width: 1200px;
    height: 930px;
  }
  .card {
    position: absolute;
    left: 290px;
    width: 620px;
    height: 354px;
    background: var(--card);
    border-radius: 22px;
    box-shadow: 0 14px 34px rgba(0,0,0,0.45);
  }
  .card--front { top: 86px; }
  .card--back { top: 490px; }

  .brand-name {
    font-family: "Playfair Display", Georgia, serif;
    font-weight: 500;
    color: var(--pink);
    line-height: 1.05;
    letter-spacing: 0.5px;
  }
  .brand-name span { display: block; }

  .card--front .brand-name {
    position: absolute;
    left: 0; right: 0;
    top: 108px;
    text-align: center;
    font-size: 44px;
  }
  .front-website {
    position: absolute;
    left: 0; right: 0;
    bottom: 44px;
    text-align: center;
    font-family: "Montserrat", Arial, sans-serif;
    font-size: 13px;
    letter-spacing: 1.6px;
    color: var(--line-grey);
  }

  .card--back .brand-name {
    position: absolute;
    left: 54px;
    top: 126px;
    width: 220px;
    text-align: center;
    font-size: 34px;
  }
  .divider {
    position: absolute;
    left: 300px;
    top: 96px;
    width: 1px;
    height: 162px;
    background: var(--pink-soft);
  }
  .contact {
    position: absolute;
    left: 330px;
    top: 102px;
    font-family: "Montserrat", Arial, sans-serif;
    color: var(--ink-grey);
  }
  .contact__name {
    font-family: "Playfair Display", Georgia, serif;
    font-weight: 500;
    font-size: 24px;
    color: var(--pink);
    letter-spacing: 0.5px;
    text-transform: uppercase;
  }
  .contact__role {
    font-size: 15px;
    margin-top: 2px;
    margin-bottom: 14px;
  }
  .contact__list { list-style: none; }
  .contact__item {
    display: flex;
    align-items: center;
    gap: 10px;
    font-size: 15px;
    margin-bottom: 7px;
  }
  .contact__icon { width: 12px; height: 12px; flex: none; }
  .contact__accent { color: var(--pink); }
</style>
</head>
<body>
<main class="stage">

  <section class="card card--front" aria-label="Card front">
    <div class="brand-name"><span>Lorna Tess</span><span>Tresses</span></div>
    <p class="front-website">www.lornatesstresses.example</p>
  </section>

  <section class="card card--back" aria-label="Card back">
    <div class="brand-name"><span>Lorna Tess</span><span>Tresses</span></div>
    <div class="divider"></div>
    <div class="contact">
      <p class="contact__name">Dana Whitfield</p>
      <p class="contact__role">Director</p>
      <ul class="contact__list">
        <li class="contact__item">
          <svg class="contact__icon" viewBox="0 0 24 24" aria-hidden="true">
            <path fill="#e34298" d="M6.6 10.8a15.2 15.2 0 0 0 6.6 6.6l2.2-2.2a1 1 0 0 1 1-.25 11.4 11.4 0 0 0 3.6.57 1 1 0 0 1 1 1V20a1 1 0 0 1-1 1A17 17 0 0 1 3 4a1 1 0 0 1 1-1h3.5a1 1 0 0 1 1 1c0 1.25.2 2.45.57 3.57a1 1 0 0 1-.25 1z"/>
          </svg>
          582 907 3365
        </li>
        <li class="contact__item">
          <svg class="contact__icon" viewBox="0 0 12 12" aria-hidden="true">
            <circle cx="6" cy="6" r="5" fill="none" stroke="#e34298" stroke-width="1.6"/>
          </svg>
          @lorna.tess.tresses__
        </li>
        <li class="contact__item">
          <svg class="contact__icon" viewBox="0 0 12 12" aria-hidden="true">
            <circle cx="6" cy="6" r="5.5" fill="#e34298"/>
          </svg>
          <span>www.<span class="contact__accent">lornatesstresses</span>.example</span>
        </li>
      </ul>
    </div>
  </section>

</main>
</body>
</html>
```